Tamarack Hearth Partners Business Card

Looking for a new business card layout. We are a real estate firm w/ a logo, old design attached. Must keep the same elements on there, just need a fresh look and possible some foil accents. Looking for a simpler design w/ more modern style.

Target Market(s)

Real Estate clients

Industry/Entity Type

Real Estate Agent

Contact Information for Business Card

see attached

Font styles to use
Sans Serif

Requirements
Must have
• all elements on current biz card
Nice to have
• modern look, simpler than we have!
Should not have
• no serif fonts

```html
<!DOCTYPE html>
<html lang="en">
<head>
<meta charset="utf-8">
<title>Tamarack Hearth Partners Business Card</title>
<link rel="stylesheet" href="https://fonts.googleapis.com/css2?family=Montserrat:wght@400;500;700;800&display=swap">
<style>
  :root {
    --ink: #0d0d0d;
    --paper: #ffffff;
    --stage: #e9e6e2;
    --muted: #2b2b2b;
    --rule: #111111;
  }
  * { box-sizing: border-box; margin: 0; padding: 0; }
  html, body { width: 1200px; height: 909px; overflow: hidden; }
  body {
    background: var(--stage);
    font-family: "Montserrat", sans-serif;
    position: relative;
  }
  .card {
    position: absolute;
    width: 520px;
    height: 297px;
    overflow: hidden;
    box-shadow: 0 6px 18px rgba(0,0,0,0.18);
  }
  .card--back {
    left: 50px; top: 306px;
    background: linear-gradient(135deg, #1c1c1c 0%, var(--ink) 60%, #050505 100%);
    display: flex; align-items: center; justify-content: center;
  }
  .card--front { left: 630px; top: 306px; background: var(--paper); }

  .wordmark {
    font-weight: 800;
    text-transform: uppercase;
    line-height: 0.95;
    letter-spacing: 0.02em;
  }
  .card--back .wordmark { color: var(--paper); font-size: 36px; text-align: left; }

  .card--front .wordmark {
    position: absolute; left: 34px; top: 50px;
    color: var(--ink); font-size: 19px;
  }

  .band-main {
    position: absolute; left: 0; top: 128px;
    width: 390px; height: 46px; background: var(--ink);
  }
  .band-top {
    position: absolute; right: 0; top: 36px;
    width: 90px; height: 30px; background: var(--ink);
  }
  .agent {
    position: absolute; left: 34px; top: 132px; color: var(--paper);
  }
  .agent__name { font-weight: 800; font-size: 18px; line-height: 1.1; }
  .agent__title { font-weight: 400; font-size: 11px; margin-top: 2px; }

  .portrait {
    position: absolute; left: 372px; top: 24px;
    width: 128px; height: 196px;
    background: linear-gradient(180deg, #d9c7a2 0%, #e6c8ae 45%, #3fc4c3 75%, #2fb6b6 100%);
  }
  .portrait-rule {
    position: absolute; left: 372px; top: 220px; width: 138px; height: 1px; background: var(--rule);
  }

  .contacts {
    position: absolute; left: 34px; top: 190px;
    list-style: none; font-size: 11px; color: var(--muted); line-height: 14px;
  }
  .contacts li { display: flex; align-items: center; gap: 7px; }
  .contacts svg { width: 9px; height: 9px; flex: none; }

  .divider {
    position: absolute; left: 34px; top: 254px; width: 440px; height: 1px; background: var(--rule);
  }
  .address {
    position: absolute; left: 34px; top: 264px;
    display: flex; align-items: center; gap: 8px;
    font-size: 12px; color: var(--muted);
  }
  .address svg { width: 10px; height: 13px; }
</style>
</head>
<body>

  <section class="card card--back" aria-label="Card back">
    <div class="wordmark">Tamarack Hearth<br>Partners</div>
  </section>

  <section class="card card--front" aria-label="Card front">
    <div class="band-top"></div>
    <div class="wordmark">Tamarack Hearth<br>Partners</div>
    <div class="band-main"></div>
    <div class="agent">
      <div class="agent__name">Dana Whitfield</div>
      <div class="agent__title">Principal Broker</div>
    </div>

    <div class="portrait" role="img" aria-label="Portrait photo of the broker"></div>
    <div class="portrait-rule"></div>

    <ul class="contacts">
      <li>
        <svg viewBox="0 0 10 10"><path d="M2 1l2 2-1 1.2c.6 1.2 1.6 2.2 2.8 2.8L7 6l2 2-1.2 1.5C4.5 9 1 5.5.5 2.2z" fill="#111"/></svg>
        555.201.3340 (Office)
      </li>
      <li>
        <svg viewBox="0 0 10 10"><rect x="2.5" y="0.5" width="5" height="9" rx="1" fill="none" stroke="#111"/><circle cx="5" cy="8" r="0.6" fill="#111"/></svg>
        555.201.8817 (Cell)
      </li>
      <li>
        <svg viewBox="0 0 10 10"><rect x="0.5" y="2" width="9" height="6" fill="#111"/><path d="M0.5 2l4.5 3.5L9.5 2" fill="none" stroke="#fff" stroke-width="0.8"/></svg>
        dana@tamarackhearth.com
      </li>
      <li>
        <svg viewBox="0 0 10 10"><circle cx="5" cy="5" r="4.3" fill="none" stroke="#111"/><path d="M.7 5h8.6M5 .7c-2.4 2.6-2.4 6 0 8.6M5 .7c2.4 2.6 2.4 6 0 8.6" fill="none" stroke="#111" stroke-width="0.7"/></svg>
        TamarackHearth-Homes.com
      </li>
    </ul>

    <div class="divider"></div>
    <div class="address">
      <svg viewBox="0 0 10 13"><path d="M5 0C2.2 0 0 2.2 0 5c0 3.5 5 8 5 8s5-4.5 5-8C10 2.2 7.8 0 5 0z" fill="#111"/><circle cx="5" cy="5" r="1.8" fill="#fff"/></svg>
      418 Juniper Ave Bend, OR 97701
    </div>
  </section>

</body>
</html>
```